Buchcover-Design für Fantasy-Serie
Inspirierte und saubere Umsetzung, sowie kundenorientiert auch bei Sonderwünschen.
Zielgruppe
Buchverlag (Kleinstverlag). Wir verlegen Bücher aus den Genres Fantasy / SciFi / Thriller und Kriminalroman, sowie spezielle thematische Ausgaben. Kern unserer Tätigkeit ist die Wiederveröffentlichung der Nebelreich-Chronik des deutschen Fantasy Autors Bertold Kamin sowie eine SciFi Serie des deutschen Autor Juno Pfalzreit. Wir suchen genretypische Cover mit Whow-Effekt.
Aufgabenstellung
Bei unserem ersten Auftrag handelt es sich um eine Fantasy Serie, bestehend aus 8 Bänden, welche vorwiegend als Kindle / eBook aber auch als Paperback veröffentlicht werden. Das Titelmotiv stammt jedes Mal von Mathieu Dorland (lizensiert) und ändert sich bei jedem Buch. Der Titel muss daher von uns bearbeitbar sein.
das EBook hat die üblichen Maße: 1600x2560, 72 dpi
Print wird voraussichtl. 12x19, aber wir benötigen nur den Titel in 300 DPI (identisch mit Ebook lediglich höhere Auflösung).
Text:
(Autorenname): Bertold Kamin
(Buchtitel): Der Orden von Quelmar
(Titelzusatz): Erster Roman der Nebelreich-Chronik
(Gattung): Roman
(Verlagslogo): Wahlweise kleines oder großes Logo, farblich angepasst
Hinweis: bei Auftrag wird das Titelbild in hoher Auflösung von uns geliefert.

```html
<!DOCTYPE html>
<html lang="de">
<head>
<meta charset="utf-8">
<title>Der Orden von Quelmar – Bertold Kamin</title>
<link rel="stylesheet" href="https://fonts.googleapis.com/css2?family=Cinzel:wght@400;500&display=swap">
<style>
  :root {
    --stage: #d9dde3;
    --night: #1a2234;
    --stone: #2f3c57;
    --slate: #4a5875;
    --haze: #cdbfc8;
    --snow: #eef1f6;
    --type: #e8eef7;
    --type-glow: rgba(160, 185, 225, 0.6);
  }
  html, body {
    margin: 0;
    width: 1200px;
    height: 1200px;
    overflow: hidden;
    background: var(--stage);
  }
  .canvas {
    width: 1200px;
    height: 1200px;
    display: flex;
    align-items: center;
    justify-content: center;
  }
  .cover {
    position: relative;
    width: 736px;
    height: 1104px;
    overflow: hidden;
    background: var(--night);
    font-family: "Cinzel", serif;
    font-weight: 400;
    color: var(--type);
  }
  .cover-art {
    position: absolute;
    inset: 0;
    width: 100%;
    height: 100%;
  }
  .cover-line {
    position: absolute;
    left: 0;
    right: 0;
    margin: 0;
    text-align: center;
    line-height: 1;
    white-space: nowrap;
  }
  .series-line {
    top: 60px;
    font-size: 18px;
    letter-spacing: 0.04em;
    text-shadow: 0 0 6px var(--type-glow);
  }
  .author {
    top: 104px;
    font-size: 70px;
    letter-spacing: 0.17em;
    padding-left: 0.17em;
    text-shadow: 0 0 14px var(--type-glow);
  }
  .title {
    position: absolute;
    inset: 0;
    margin: 0;
    font-weight: 400;
    text-shadow: 0 0 16px var(--type-glow);
  }
  .title-small {
    top: 414px;
    font-size: 64px;
    letter-spacing: 0.05em;
  }
  .title-main {
    top: 512px;
    font-size: 84px;
    letter-spacing: 0.04em;
  }
  .title-tail {
    top: 626px;
    font-size: 84px;
    letter-spacing: 0.04em;
  }
  .title-tail .joiner {
    font-size: 58px;
    margin-right: 0.15em;
  }
  .genre {
    top: 1052px;
    font-size: 28px;
    letter-spacing: 0.06em;
    text-shadow: 0 0 6px var(--type-glow);
  }
  .publisher {
    position: absolute;
    left: 686px;
    top: 760px;
    margin: 0;
    font-size: 24px;
    font-weight: 500;
    letter-spacing: 0.1em;
    line-height: 1;
    color: var(--snow);
    writing-mode: vertical-rl;
    transform: rotate(180deg);
  }
</style>
</head>
<body>
<main class="canvas">
  <article class="cover">
    <svg class="cover-art" viewBox="0 0 736 1104" preserveAspectRatio="none" role="img" aria-label="Titelillustration: riesige steinerne Gestalt in nebligen Bergen über einer verschneiten Felsklippe mit kleinem Wanderer">
      <defs>
        <linearGradient id="art-base" x1="0" y1="0" x2="1" y2="1">
          <stop offset="0" stop-color="#232d44"/>
          <stop offset="0.45" stop-color="#36445f"/>
          <stop offset="1" stop-color="#1b2335"/>
        </linearGradient>
        <radialGradient id="art-mist" cx="0.38" cy="0.3" r="0.42">
          <stop offset="0" stop-color="#d8c6cc" stop-opacity="0.75"/>
          <stop offset="0.5" stop-color="#9d98ab" stop-opacity="0.4"/>
          <stop offset="1" stop-color="#9d98ab" stop-opacity="0"/>
        </radialGradient>
        <radialGradient id="art-stone" cx="0.5" cy="0.62" r="0.35">
          <stop offset="0" stop-color="#1f2a40" stop-opacity="0.85"/>
          <stop offset="1" stop-color="#1f2a40" stop-opacity="0"/>
        </radialGradient>
        <radialGradient id="art-snow" cx="0.82" cy="0.76" r="0.3">
          <stop offset="0" stop-color="#f1f3f8" stop-opacity="0.95"/>
          <stop offset="0.45" stop-color="#c9d0de" stop-opacity="0.55"/>
          <stop offset="1" stop-color="#c9d0de" stop-opacity="0"/>
        </radialGradient>
        <radialGradient id="art-drift" cx="0.18" cy="0.8" r="0.25">
          <stop offset="0" stop-color="#aebad0" stop-opacity="0.45"/>
          <stop offset="1" stop-color="#aebad0" stop-opacity="0"/>
        </radialGradient>
        <linearGradient id="art-shade" x1="0" y1="0" x2="0" y2="1">
          <stop offset="0" stop-color="#141b2a" stop-opacity="0.55"/>
          <stop offset="0.22" stop-color="#141b2a" stop-opacity="0"/>
          <stop offset="0.85" stop-color="#141b2a" stop-opacity="0"/>
          <stop offset="1" stop-color="#141b2a" stop-opacity="0.6"/>
        </linearGradient>
      </defs>
      <rect width="736" height="1104" fill="url(#art-base)"/>
      <rect width="736" height="1104" fill="url(#art-mist)"/>
      <rect width="736" height="1104" fill="url(#art-stone)"/>
      <rect width="736" height="1104" fill="url(#art-snow)"/>
      <rect width="736" height="1104" fill="url(#art-drift)"/>
      <rect width="736" height="1104" fill="url(#art-shade)"/>
    </svg>

    <p class="cover-line series-line">Erster Roman der Nebelreich-Chronik</p>
    <p class="cover-line author">Bertold Kamin</p>
    <h1 class="title">
      <span class="cover-line title-small">Der</span>
      <span class="cover-line title-main">Orden</span>
      <span class="cover-line title-tail"><span class="joiner">von</span>Quelmar</span>
    </h1>
    <p class="cover-line genre">Roman</p>
    <p class="publisher">VELMORUM</p>
  </article>
</main>
</body>
</html>
```